Mesa Lantern Billboard

We are looking to have a new billboard design for our Casual Restaurant chain. We are a steakhouse chain that is very casual. You can visit our website at: www.mesalantern.example to get an idea of our menu. We are looking to have some new billboard ideas for our steakhouse so that we can communicate our concept to customers that are passing by the billboard. I have attached some items to give you a feel for our concept. The Billboard will be 14'X48'. I look forward to hearing from you. Derek

```html
<!DOCTYPE html>
<html lang="en">
<head>
<meta charset="utf-8">
<title>Mesa Lantern Billboard</title>
<link rel="stylesheet" href="https://fonts.googleapis.com/css2?family=Rubik+Dirt&display=swap">
<style>
  :root {
    --page: #e9e6e1;
    --board: #fbfaf8;
    --tan: #c2a97f;
    --tan-dark: #a88e63;
    --denim-light: #8d8a86;
    --denim-dark: #4a4744;
    --brand-red: #b3191e;
  }
  html, body {
    margin: 0;
    padding: 0;
    width: 1200px;
    height: 689px;
    overflow: hidden;
    background: var(--page);
  }
  .billboard {
    position: absolute;
    left: 40px;
    top: 144px;
    width: 1120px;
    height: 400px;
    background: var(--board);
    overflow: hidden;
    box-shadow: 0 2px 10px rgba(0,0,0,0.18);
  }
  .billboard__photo {
    position: absolute;
    left: 0;
    top: 0;
    width: 600px;
    height: 400px;
  }
  .headline {
    position: absolute;
    left: 540px;
    top: 34px;
    width: 500px;
    margin: 0;
    font-family: "Rubik Dirt", system-ui, sans-serif;
    font-weight: 400;
    color: var(--tan);
    text-align: center;
    line-height: 0.9;
    letter-spacing: 1px;
  }
  .headline__line {
    display: block;
  }
  .headline__line--top {
    font-size: 104px;
    margin-left: 40px;
  }
  .headline__line--bottom {
    font-size: 112px;
  }
  .brand {
    position: absolute;
    left: 870px;
    top: 222px;
    width: 220px;
    display: flex;
    flex-direction: column;
    align-items: center;
    gap: 10px;
  }
  .brand__dot {
    width: 62px;
    height: 62px;
    border-radius: 50%;
    background: var(--brand-red);
  }
  .brand__name {
    font-family: "Rubik Dirt", system-ui, sans-serif;
    font-size: 36px;
    color: var(--brand-red);
    white-space: nowrap;
  }
</style>
</head>
<body>
  <main class="billboard">
    <svg class="billboard__photo" viewBox="0 0 600 400" role="img"
         aria-label="Photograph of a hand in a denim jacket pocket gripping a silver fork">
      <defs>
        <linearGradient id="denim" x1="0" y1="0" x2="1" y2="1">
          <stop offset="0" stop-color="var(--denim-light)"/>
          <stop offset="0.55" stop-color="#6b6864"/>
          <stop offset="1" stop-color="var(--denim-dark)"/>
        </linearGradient>
      </defs>
      <path d="M0 0 H312 C360 90 470 230 575 400 H0 Z" fill="url(#denim)"/>
    </svg>

    <h1 class="headline">
      <span class="headline__line headline__line--top">Forks</span>
      <span class="headline__line headline__line--bottom">included</span>
    </h1>

    <div class="brand">
      <span class="brand__dot"></span>
      <span class="brand__name">Mesa Lantern</span>
    </div>
  </main>
</body>
</html>
```